BrambleCove.Lawyer, a new website for Tobin.

Looking for a professional web site for my small country law firm.
I have a logo, chart, map, my photo, office photo, google analytics code, my drone video on YouTube, "Ridgewell Cove Morning Drift, also on www.ridgewellcove.guide", and text content. I am figuring out how to get those into digital forms.
First page needs a professional look. Here's where I am really hoping for your skill set.
Banner should be well designed so as to "ease" the viewer into confidence in my firm
Prefer the "white backround", less cluttered style of design.
My office has been in Ridgewell Center, main and only town of Ridgewell Peninsula, for 25 years, with emphasis on real property matters. Naturally land lasts longer than people, so estates, trusts and succession issues are relevant.
Local KP is the heart of southern Bramble Cove, 75 miles of spectacular residential waterfront. We have the best land, waterfront, beaches and views in Bramble Cove, however of course Seattle and the San Juan Islands could not be disregarded. It's that we have the most privacy, the best old growth Doug Firs, wildlife and low population density.
Bramble Cove conditions are very specific for residential development.
One must consider:
Topography, hydro-geology, geomorphology, hill slope stability, soils must support septic systems, individual wells, prescriptive, express and implied easement issues, boundary lines don't always line up with surveys or expectations, or historic use, thus adverse possession abounds environmentally protected shorelines and wetlands, all challenges, but ohh.., the views and unique, world class waterfront.
Everyone who lives on Bramble Cove is convinced they live in the most beautiful and spectacular place in the world, and we're all correct.

Target Market(s)

Members of the Halvern-Dunmore County Bar Association, and more distant counsel seeking consultation re: local conditions.
Also, I decided it was time to have a website, so a reference place to direct clients.
I like the professional sound of .lawyer vs. commercial sound of .com.

Industry/Entity Type

Law Firm

Coding

Coded - Design and coding required

Number of Pages Required

5+ page

Other font styles liked:
• That newly created "web" font everyone seems to be usIng

Colors
32b8a4
3377b5

Requirements
Must have
• A strong first page with my photo and Bramble Cove chart professionally created.
• A page I have ready with local links.
• A "How to find me page", which should have a map, and photo of my office, which I can make with the preloaded templates the host provides.
• A "This is what I do page", with some testimonials, which I can do via said templates or preferably by professionals.
Nice to have
• Clean look.
• Consistent looks to pages.
• First comment I got back talked about just designing one page, and if requires $340.00, so be it.
• Typical local sites have 4/5 pages, so perhaps a "fill-able" generic pages, I can build myself.
• Ideally, I would step into a working site I can edit myself.
• Not looking for e-commerce site, but the remainder of language the "Smart" professional used is unknown to me.
• Bit out of my element here, hoping for guidance.
Should not have
• Clutter

```html
<!DOCTYPE html>
<html lang="en">
<head>
<meta charset="utf-8">
<title>BrambleCove.Lawyer</title>
<link href="https://fonts.googleapis.com/css2?family=Arvo:wght@400;700&family=Open+Sans:wght@400;600&family=Kaushan+Script&display=swap" rel="stylesheet">
<style>
:root{
  --brand:#2b3790;
  --button:#3a47b9;
  --button-edge:#26308a;
  --ink:#222;
  --body:#555;
  --muted:#9a9a9a;
  --pale:#f1f1f1;
  --dark:#2b2b2d;
  --darker:#1e1e20;
  --white:#fff;
}
*{box-sizing:border-box;margin:0;padding:0}
html,body{width:1200px;height:3046px;overflow:hidden}
body{position:relative;background:var(--white);font-family:"Open Sans",Arial,sans-serif;color:var(--body)}
.abs{position:absolute}
.serif{font-family:"Arvo",Georgia,serif}
.btn{position:absolute;display:flex;align-items:center;justify-content:center;border-radius:26px;background:var(--button);color:var(--white);font-family:"Arvo",Georgia,serif;font-size:16px;letter-spacing:.5px;box-shadow:3px 3px 0 var(--button-edge)}

/* top bar */
.topbar{left:0;top:0;width:1200px;height:53px;background:var(--brand);color:var(--white);font-size:16px}
.topbar .item{position:absolute;top:15px;display:flex;align-items:center;gap:10px}
.social-top{position:absolute;top:11px;right:72px;display:flex;gap:6px}
.social-top span{width:30px;height:30px;border-radius:50%;background:var(--white)}

/* header */
.header{left:0;top:53px;width:1200px;height:103px;background:var(--white)}
.logo{position:absolute;left:81px;top:22px;display:flex;align-items:center;gap:12px}
.logo-dot{width:64px;height:64px;border-radius:50%;background:var(--brand)}
.logo-name{font-family:"Arvo",Georgia,serif;font-size:26px;color:var(--brand)}
.nav{position:absolute;top:42px;font-family:"Arvo",Georgia,serif;font-size:15px;color:#555;letter-spacing:.5px}
.nav.active{color:var(--brand)}

/* hero */
.hero{left:0;top:156px;width:1200px;height:500px;background:linear-gradient(180deg,#4f7fa6 0%,#8fa9c2 30%,#c8a99a 45%,#8e9a5a 55%,#5d7a2e 75%,#3f4a2c 100%);text-align:center}
.hero-kicker{position:absolute;left:0;width:1200px;top:114px;font-family:"Arvo",Georgia,serif;font-size:22px;color:#111;letter-spacing:1px}
.hero-title{position:absolute;left:0;width:1200px;top:150px;font-family:"Arvo",Georgia,serif;font-size:52px;letter-spacing:1px;color:#111}
.hero-title b{color:var(--brand);font-weight:400}
.hero-text{position:absolute;left:0;width:1200px;top:222px;font-size:17px;line-height:28px;color:#111}

/* feature boxes */
.features{left:132px;top:599px;width:936px;height:124px;background:var(--white);border:1px solid #ddd;display:flex}
.feature{flex:1;position:relative;border-right:1px solid #ddd}
.feature:last-child{border-right:0}
.feature .icon{position:absolute;left:22px;top:24px;width:58px;height:68px;border-radius:29px 29px 6px 6px;background:#444}
.feature h3{position:absolute;left:98px;top:26px;font-family:"Arvo",Georgia,serif;font-weight:400;font-size:17px;color:#111}
.feature .btn{left:94px;top:56px;width:178px;height:40px;font-size:15px;font-family:"Open Sans",Arial,sans-serif}

/* civil law */
.center{left:0;width:1200px;text-align:center}
.eyebrow{font-family:"Arvo",Georgia,serif;font-size:16px;color:#333}
.eyebrow em{font-style:normal;color:var(--brand)}
.section-title{font-family:"Arvo",Georgia,serif;font-size:42px;color:#111;letter-spacing:1px}
.intro{left:199px;top:874px;width:802px;text-align:center;font-size:13.5px;line-height:21px;color:#666}
.consult{left:256px;top:1021px;width:686px;height:85px;background:#ececec}
.consult p{position:absolute;left:35px;top:31px;font-family:"Arvo",Georgia,serif;font-size:15.5px;color:#333}
.consult .btn{left:420px;top:18px;width:212px;height:50px}

/* practice area */
.practice{left:0;top:1157px;width:1200px;height:656px;background:linear-gradient(135deg,#3b3a3c,#2a2a2c 50%,#3a3a3c)}
.practice .eyebrow{color:#ccc}
.practice .eyebrow em{color:#999}
.practice-title{color:#bbb}
.portrait{left:0;top:61px;width:396px;height:595px;background:linear-gradient(180deg,#3c3530,#1c1a1c);}
.card{position:absolute;background:#f3f3f3}
.card.white{background:#fff}
.pitem{position:absolute;height:120px}
.pitem .num{position:absolute;right:14px;top:10px;font-family:"Arvo",Georgia,serif;font-size:28px;color:#e3e3e3}
.pitem svg{position:absolute;left:22px;top:40px}
.pitem .label{position:absolute;left:84px;top:52px;font-family:"Arvo",Georgia,serif;font-size:14px;color:#333;letter-spacing:.3px}
.pitem.stack svg{left:50%;transform:translateX(-50%);top:26px}
.pitem.stack .label{left:0;right:0;top:88px;text-align:center}

/* blog */
.blog-card{position:absolute;top:1991px;width:333px;height:187px;color:var(--white)}
.blog-card .meta{position:absolute;left:26px;font-size:11.5px;color:#eee}
.blog-card h4{position:absolute;left:26px;font-family:"Arvo",Georgia,serif;font-size:16px}
.blog-card p{position:absolute;left:26px;width:280px;font-size:13px;line-height:21px}

/* signup */
.signup{left:0;top:2241px;width:1200px;height:333px;background:linear-gradient(135deg,#2c2c2e,#3b3d40 60%,#2a2a2c)}
.signup .need{position:absolute;left:80px;top:64px;font-family:"Arvo",Georgia,serif;font-size:19px;color:var(--white)}
.signup h2{position:absolute;left:80px;top:80px;font-family:"Arvo",Georgia,serif;font-weight:400;font-size:52px;color:var(--white);letter-spacing:2px}
.script{position:absolute;font-family:"Kaushan Script",cursive;color:var(--white)}
.field{position:absolute;background:var(--white);border-radius:3px;font-size:12.5px;color:#666;padding:9px 12px}
.inquire{position:absolute;left:891px;top:221px;width:215px;height:49px;border-radius:25px;background:#8e8e8e;color:#eee;display:flex;align-items:center;justify-content:center;font-family:"Arvo",Georgia,serif;font-size:15px;box-shadow:3px 3px 0 #5a5a5a}

/* partners */
.partners{left:0;top:2574px;width:1200px;height:136px;background:var(--white);display:flex;justify-content:space-around;align-items:center;padding:0 70px}
.partners span{width:140px;height:56px;border-radius:28px;background:#d5d5d5}

/* footer */
.footer{left:0;top:2710px;width:1200px;height:336px;background:linear-gradient(180deg,#2a2320,#1f1c1b);color:#bbb}
.fcol{position:absolute;top:52px;width:300px;text-align:center;font-size:15px;line-height:22px}
.fcol svg{display:block;margin:0 auto 10px}
.fline{position:absolute;left:0;top:177px;width:1200px;height:1px;background:#555}
.fbtn{position:absolute;top:153px;width:207px;height:49px;border-radius:25px;display:flex;align-items:center;justify-content:center;font-family:"Arvo",Georgia,serif;font-size:15px}
.social-foot{position:absolute;top:235px;left:498px;display:flex;gap:14px}
.social-foot span{width:40px;height:40px;background:var(--white)}
.copy{position:absolute;left:0;width:1200px;top:295px;text-align:center;font-size:14px;color:#aaa}
</style>
</head>
<body>

<div class="abs topbar">
  <div class="item" style="left:78px">
    <svg width="18" height="18" viewBox="0 0 24 24"><path fill="#fff" d="M6.6 10.8a15 15 0 0 0 6.6 6.6l2.2-2.2c.3-.3.7-.4 1-.2 1.1.4 2.3.6 3.6.6.6 0 1 .4 1 1V20c0 .6-.4 1-1 1A17 17 0 0 1 3 4c0-.6.4-1 1-1h3.5c.6 0 1 .4 1 1 0 1.3.2 2.5.6 3.6.1.3 0 .7-.2 1z"/></svg>
    555-014-2290
  </div>
  <div class="item" style="left:250px">
    <svg width="20" height="16" viewBox="0 0 20 16"><rect x="1" y="1" width="18" height="14" fill="none" stroke="#fff" stroke-width="2"/><path d="M1 1l9 7 9-7" fill="none" stroke="#fff" stroke-width="2"/></svg>
    tobin@bramblecove.lawyer
  </div>
  <div class="social-top"><span></span><span></span><span></span><span></span></div>
</div>

<div class="abs header">
  <div class="logo"><span class="logo-dot"></span><span class="logo-name">BrambleCove.Lawyer</span></div>
  <span class="nav active" style="left:536px">HOME</span>
  <span class="nav" style="left:621px">ABOUT US</span>
  <span class="nav" style="left:739px">OUR SERVICES</span>
  <span class="nav" style="left:893px">CAREERS</span>
  <span class="nav" style="left:1003px">CONTACT US</span>
</div>

<section class="abs hero" role="img" aria-label="Country road running through green fields under a wide evening sky">
  <div class="hero-kicker">WE ARE DONE EXCELLENT JOB</div>
  <h1 class="hero-title" style="font-weight:400"><b>GET</b> LEGAL <b>HELP IMMEDIATELY</b></h1>
  <p class="hero-text">Lorem Ipsum is simply dummy text of the printing and typesetting industry.<br>Lorem Ipsum has been the.</p>
  <div class="btn" style="left:449px;top:318px;width:305px;height:50px;font-size:18px">NEED LEGAL ASSISTANCE</div>
</section>

<div class="abs features">
  <div class="feature">
    <span class="icon" role="img" aria-label="Lawyer icon"></span>
    <h3>REQUEST A LAWYER</h3>
    <div class="btn">Ask For Question</div>
  </div>
  <div class="feature">
    <span class="icon" role="img" aria-label="Investigator icon"></span>
    <h3>CASE INVESTIGATION</h3>
    <div class="btn">Lawyer Strugle</div>
  </div>
  <div class="feature">
    <span class="icon" role="img" aria-label="Directory icon" style="background:#3a47b9"></span>
    <h3>SEARCH DIRECTORY</h3>
    <div class="btn">People Search</div>
  </div>
</div>

<div class="abs center eyebrow" style="top:786px"><em>25 Years</em> Experience In</div>
<h2 class="abs center section-title" style="top:806px;font-weight:400">GENERAL CIVIL LAW</h2>
<p class="abs intro">In the heart of Bramble Cove, Ridgewell Peninsula's 75 miles of prime residential waterfront properties require experienced counsel with a deft touch. I started my office here in Ridgewell Center, Ridgewell Peninsula's main "town" in June, 1990, and focused on real property during the last 25 years. Quiet Titles, boundary lines disputes, easements, road and water maintenance agreements, meander lines, environmental concerns, zoning and variances, along with various conveyance and estate succession issues and techniques.</p>
<div class="abs consult">
  <p>Get Your FREE Consultation - Available 24/7</p>
  <div class="btn">HIRE IMMEDIATELY</div>
</div>

<section class="abs practice">
  <div class="abs center eyebrow" style="top:62px">25 Years <em>Experience</em></div>
  <h2 class="abs center section-title practice-title" style="top:98px;font-weight:400">PRACTICE AREA</h2>
  <div class="abs portrait" role="img" aria-label="Young lawyer in a black robe reading a red law book"></div>

  <div class="card white" style="left:440px;top:276px;width:192px;height:272px">
    <div class="pitem" style="left:0;top:0;width:192px">
      <span class="num">01</span>
      <svg width="60" height="40" viewBox="0 0 60 40" style="left:40px;top:36px"><circle cx="16" cy="24" r="12" fill="none" stroke="#2b3790" stroke-width="4"/><circle cx="44" cy="24" r="12" fill="none" stroke="#2b3790" stroke-width="4"/><path d="M28 18h4" stroke="#2b3790" stroke-width="4"/></svg>
      <span class="label" style="left:36px;top:90px;color:#2b3790">CRIMINAL IAW</span>
    </div>
    <div class="pitem" style="left:0;top:136px;width:192px">
      <span class="num">06</span>
      <svg width="48" height="48" viewBox="0 0 48 48" style="left:26px;top:30px"><path d="M24 4L46 44H2z" fill="none" stroke="#555" stroke-width="4" stroke-linejoin="round"/><rect x="22" y="18" width="4" height="14" fill="#555"/><rect x="22" y="36" width="4" height="4" fill="#555"/></svg>
      <span class="label" style="left:84px;top:50px">ACCIDENT IAW</span>
    </div>
  </div>

  <div class="card" style="left:644px;top:201px;width:270px;height:378px">
    <div class="pitem" style="left:0;top:0;width:270px">
      <span class="num">02</span>
      <svg width="62" height="40" viewBox="0 0 62 40" style="left:24px;top:36px"><circle cx="20" cy="22" r="14" fill="none" stroke="#666" stroke-width="4"/><circle cx="40" cy="22" r="14" fill="none" stroke="#666" stroke-width="4"/></svg>
      <span class="label" style="left:96px;top:50px">DIVORCE IAW</span>
    </div>
    <div class="pitem" style="left:0;top:116px;width:270px">
      <span class="num">05</span>
      <svg width="62" height="56" viewBox="0 0 62 56" style="left:24px;top:22px"><g fill="#666"><rect x="4" y="10" width="22" height="8" rx="3"/><rect x="4" y="20" width="22" height="8" rx="3"/><rect x="4" y="30" width="22" height="8" rx="3"/><rect x="4" y="40" width="22" height="8" rx="3"/><rect x="28" y="24" width="20" height="8" rx="3"/><rect x="28" y="34" width="20" height="8" rx="3"/></g><circle cx="48" cy="42" r="12" fill="#555" stroke="#f3f3f3" stroke-width="3"/><path d="M48 35v14" stroke="#fff" stroke-width="2"/></svg>
      <span class="label" style="left:96px;top:50px">CORPORATE IAW</span>
    </div>
    <div class="pitem" style="left:0;top:250px;width:270px">
      <span class="num">07</span>
      <svg width="52" height="44" viewBox="0 0 52 44" style="left:109px;top:14px"><rect x="2" y="10" width="48" height="32" rx="3" fill="#666"/><rect x="18" y="2" width="16" height="10" rx="2" fill="none" stroke="#666" stroke-width="4"/><rect x="2" y="22" width="48" height="3" fill="#f3f3f3"/></svg>
      <span class="label" style="left:0;right:0;top:76px;text-align:center">BUSINESS IAW</span>
    </div>
  </div>

  <div class="card" style="left:914px;top:138px;width:209px;height:355px">
    <div class="pitem stack" style="left:0;top:0;width:209px;height:170px">
      <span class="num">03</span>
      <svg width="56" height="52" viewBox="0 0 56 52"><path d="M4 48V22l12 8V22l12 8V22l12 8V8h10v40z" fill="#666"/><rect x="20" y="2" width="16" height="6" fill="#666"/></svg>
      <span class="label">INDUSTRIAL IAW</span>
    </div>
    <div class="pitem stack" style="left:0;top:178px;width:209px;height:170px">
      <span class="num">04</span>
      <svg width="60" height="60" viewBox="0 0 60 60"><g fill="#666"><rect x="6" y="40" width="8" height="16"/><rect x="18" y="32" width="8" height="24"/><rect x="30" y="36" width="8" height="20"/><rect x="42" y="22" width="8" height="34"/></g><path d="M6 34l14-12 12 8 20-18" fill="none" stroke="#666" stroke-width="3"/><text x="26" y="16" font-family="Arvo,serif" font-size="18" fill="#666">$</text></svg>
      <span class="label">FINANCIAL IAW</span>
    </div>
  </div>
</section>

<div class="abs center eyebrow" style="top:1876px"><em>Recent</em> News &amp; Updates</div>
<h2 class="abs center section-title" style="top:1902px;font-weight:400">LAWFIRM BLOG</h2>

<article class="blog-card" style="left:77px;background:linear-gradient(135deg,#5a4326,#2a2118)" role="img" aria-label="Lawyer speaking in a wood-panelled courtroom">
  <span class="meta" style="top:62px">Sep 7, 2015 by Mara Ellison</span>
  <h4 style="top:84px">Blog Title</h4>
  <p style="top:120px">Lorem Ipsum is simply dummy text of the printing and typesetting industry.</p>
</article>
<article class="blog-card" style="left:432px;background:linear-gradient(135deg,#4a4a4c,#1c1c1e)" role="img" aria-label="Hands signing a document at a desk">
  <span class="meta" style="top:126px">Sep 7, 2015 by Mara Ellison</span>
  <h4 style="top:144px">Blog Title</h4>
</article>
<article class="blog-card" style="left:790px;background:linear-gradient(135deg,#8a8e96,#3a3e48)" role="img" aria-label="Team meeting around an office table">
  <span class="meta" style="top:126px">Sep 7, 2015 by Mara Ellison</span>
  <h4 style="top:144px">Blog Title</h4>
</article>

<section class="abs signup" role="img" aria-label="Laptop keyboard on a dark desk">
  <span class="need">NEED US</span>
  <h2>SIGN UP !</h2>
  <span class="script" style="left:92px;top:176px;font-size:40px;transform:rotate(-8deg)">Start Today !</span>
  <span class="script" style="left:196px;top:230px;font-size:34px;transform:rotate(-8deg)">555-014-2290</span>
  <div class="field" style="left:390px;top:63px;width:230px;height:39px">First Name</div>
  <div class="field" style="left:626px;top:63px;width:237px;height:39px">Last Name</div>
  <div class="field" style="left:869px;top:63px;width:237px;height:39px">Phone</div>
  <div class="field" style="left:390px;top:110px;width:230px;height:39px">E-Mail</div>
  <div class="field" style="left:390px;top:156px;width:230px;height:39px">Subject</div>
  <div class="field" style="left:626px;top:110px;width:480px;height:85px">Message</div>
  <div class="inquire">INQUIRE NOW</div>
</section>

<div class="abs partners" aria-label="Partner badges">
  <span></span><span></span><span></span><span></span><span></span><span></span>
</div>

<footer class="abs footer">
  <div class="fcol" style="left:95px">
    <svg width="22" height="30" viewBox="0 0 22 30"><path d="M11 1a10 10 0 0 0-10 10c0 8 10 18 10 18s10-10 10-18A10 10 0 0 0 11 1z" fill="none" stroke="#bbb" stroke-width="2.5"/><circle cx="11" cy="11" r="3.5" fill="#bbb"/></svg>
    4417 Cove Ridge Rd. N., Halvern, United States
  </div>
  <div class="fcol" style="left:450px">
    <svg width="28" height="28" viewBox="0 0 24 24"><path fill="#bbb" d="M6.6 10.8a15 15 0 0 0 6.6 6.6l2.2-2.2c.3-.3.7-.4 1-.2 1.1.4 2.3.6 3.6.6.6 0 1 .4 1 1V20c0 .6-.4 1-1 1A17 17 0 0 1 3 4c0-.6.4-1 1-1h3.5c.6 0 1 .4 1 1 0 1.3.2 2.5.6 3.6.1.3 0 .7-.2 1z"/></svg>
    555-014-2290
  </div>
  <div class="fcol" style="left:810px">
    <svg width="30" height="24" viewBox="0 0 30 24"><rect x="2" y="2" width="26" height="20" rx="2" fill="none" stroke="#bbb" stroke-width="2.5"/><path d="M2 4l13 10 13-10" fill="none" stroke="#bbb" stroke-width="2.5"/></svg>
    tobin@bramblecove.lawyer
  </div>
  <div class="fline"></div>
  <div class="fbtn" style="left:382px;background:var(--button);color:#fff;box-shadow:3px 3px 0 var(--button-edge)">APPOINT NOW</div>
  <div class="fbtn" style="left:611px;background:#2a2320;border:1px solid #666;color:#999">GO TO MAP</div>
  <div class="social-foot"><span></span><span></span><span></span><span></span></div>
  <p class="copy">© bramblecove.lawyer 2015. All Rights Reserved.</p>
</footer>

</body>
</html>
```